Splashora water park letter head

the previous one need some update and to be fresh again.
attached is the previous design and want it something along the same way
logo on top and info in the bottom
attached also the logo in all formats.

Target Market(s)

official use

Font styles to use
Sans Serif

Requirements
Must have
• logo on top and as watermark
• website : www.splashora.ae
• address : P.O.Box 3867 Dubai - UAE
• email : info@splashora.ae
• social media links : splashorame
Nice to have
• something creative on the bottom
Should not have
• no phone numbers

```html
<!DOCTYPE html>
<html lang="en">
<head>
<meta charset="utf-8">
<title>Splashora Letterhead</title>
<link rel="stylesheet" href="https://fonts.googleapis.com/css2?family=Open+Sans:wght@400;600&family=Lato:wght@400;700&display=swap">
<style>
  :root {
    --paper: #ffffff;
    --ink: #3d3d3d;
    --ink-strong: #2a2a2a;
    --brand: #2b5fc2;
    --watermark: rgba(43, 95, 194, 0.06);
    --wave-top: #27c3f3;
    --wave-bottom: #1288dc;
    --wave-line: #1f4fa8;
    --footer-text: #ffffff;
  }
  * { margin: 0; padding: 0; box-sizing: border-box; }
  html, body { width: 1040px; height: 1200px; overflow: hidden; background: var(--paper); }
  .letterhead {
    position: relative;
    width: 1040px;
    height: 1200px;
    background: var(--paper);
    font-family: "Open Sans", sans-serif;
    color: var(--ink);
    overflow: hidden;
  }
  .brand-mark {
    position: absolute;
    left: 610px; top: 78px; width: 230px;
    display: flex; align-items: center; justify-content: center; gap: 12px;
    font-family: "Open Sans", sans-serif;
    font-weight: 600;
    font-size: 40px;
    color: var(--brand);
  }
  .brand-mark .dot { width: 22px; height: 22px; border-radius: 50%; background: var(--brand); }
  .watermark {
    position: absolute;
    left: 180px; top: 610px; width: 680px;
    text-align: center;
    font-weight: 600;
    font-size: 140px;
    color: var(--watermark);
    pointer-events: none;
  }
  .letter { position: absolute; left: 87px; width: 753px; font-size: 15px; line-height: 27px; }
  .meta { top: 214px; }
  .recipient { top: 253px; line-height: 18px; }
  .salutation { top: 355px; }
  .body { top: 410px; text-align: justify; }
  .body p + p { margin-top: 27px; }
  .closing { top: 814px; }
  .signature {
    position: absolute; left: 87px; top: 858px;
    width: 215px; height: 22px;
    background: linear-gradient(90deg, rgba(60,60,60,0.12), rgba(60,60,60,0.05));
    border-radius: 2px;
  }
  .signer { position: absolute; left: 87px; top: 890px; }
  .signer-name { font-size: 19px; font-weight: 600; color: var(--ink-strong); line-height: 28px; }
  .signer-title { font-size: 15px; line-height: 22px; }
  .footer { position: absolute; left: 0; top: 1078px; width: 1040px; height: 122px; }
  .footer svg { position: absolute; inset: 0; }
  .contact {
    position: absolute; left: 87px; top: 46px;
    font-family: "Lato", sans-serif; font-size: 17px; line-height: 27px;
    color: var(--footer-text);
  }
  .social {
    position: absolute; left: 684px; top: 71px;
    display: flex; align-items: center; gap: 10px;
    font-family: "Lato", sans-serif; font-weight: 700; font-size: 13px;
    color: var(--footer-text);
  }
  .social .square { width: 16px; height: 16px; background: var(--footer-text); border-radius: 2px; }
</style>
</head>
<body>
<div class="letterhead">
  <div class="brand-mark"><span class="dot"></span>Splashora</div>
  <div class="watermark" aria-hidden="true">Splashora</div>

  <div class="letter meta">Issuing Date: May 5, 2018</div>
  <div class="letter recipient">
    Name Of Employee Mr. XYZABC<br>
    Address of Employee<br>
    Address Line 2 etc..
  </div>
  <div class="letter salutation">Dear Mr.XYZABC</div>
  <div class="letter body">
    <p>Lorem Ipsum has been the industry's standard dummy text ever since the 1500s, when an unknown printer took a galley of type and scrambled it to make a type specimen book. It has survived not only five centuries, but also the leap into electronic typesetting, remaining essentially unchanged. It was popularised in the 1960s with the release of Typeline sheets containing Lorem Ipsum passages, and more recently with desktop publishing software like Pagewright Studio including versions of Lorem Ipsum.</p>
    <p>Lorem Ipsum is simply dummy text of the printing and typesetting industry. Lorem Ipsum has been the industry's standard dummy text ever since the 1500s, when an unknown printer took a galley of type and scrambled it to make a type specimen book.</p>
    <p>It has survived not only five centuries, but also the leap into electronic typesetting, remaining essentially unchanged. It was popularised in the 1960s with the release of Typeline sheets containing Lorem IpsumIpsum passages.</p>
  </div>
  <div class="letter closing">Yours Sincerely</div>
  <div class="signature" role="img" aria-label="Handwritten signature of Marcus Hale"></div>
  <div class="signer">
    <div class="signer-name">Marcus Hale</div>
    <div class="signer-title">Managing Director</div>
  </div>

  <footer class="footer">
    <svg width="1040" height="122" viewBox="0 0 1040 122" aria-hidden="true">
      <defs>
        <linearGradient id="waveFill" x1="0" y1="0" x2="0" y2="1">
          <stop offset="0" stop-color="var(--wave-top)"/>
          <stop offset="1" stop-color="var(--wave-bottom)"/>
        </linearGradient>
      </defs>
      <path d="M0 8 C 90 30, 170 30, 250 14 S 360 24, 430 22 S 560 -6, 650 22 S 770 2, 850 8 S 980 20, 1040 4 L1040 122 L0 122 Z" fill="url(#waveFill)"/>
      <path d="M0 8 C 90 30, 170 30, 250 14 S 360 24, 430 22 S 560 -6, 650 22 S 770 2, 850 8 S 980 20, 1040 4" fill="none" stroke="var(--wave-line)" stroke-width="3"/>
    </svg>
    <div class="contact">
      P.O.Box 3867 Dubai - UAE<br>
      www.splashora.ae &nbsp;|&nbsp;info@splashora.ae
    </div>
    <div class="social"><span class="square"></span>SPLASHORAME</div>
  </footer>
</div>
</body>
</html>
```